Create look and feel for existing Web Page

Update Web Page

We have a website at http://www.usekivra.com/index-web.html. It is a single page html site, with a custom signup form. We also have a quill bay plugin at the bottom of the page. We'd like to redesign the look and feel of the entire site. We sell software to eye doctors. Also called optometrists, our software tool makes it easy for doctors to manage patients, bill, and document patient encounters. I have included our logos below.

We are looking for a new design preferably in HTML 5, CSS etc. The fields on the form on this page: http://www.usekivra.com/index-web.html

You can get screen shots of our software application at this site: http://staging.usekivra.com
username: test@samplevora.com
password: password

```html
<!DOCTYPE html>
<html lang="en">
<head>
<meta charset="utf-8">
<title>Vellisto — Optometry Office Software</title>
<link href="https://fonts.googleapis.com/css2?family=Josefin+Sans:wght@400;600;700&family=Montserrat:wght@400;500;600;700&display=swap" rel="stylesheet">
<style>
:root{
  --orange:#f7821b;
  --blue:#1a9be0;
  --ink:#222;
  --muted:#444;
  --line:#e3e3e3;
  --card-band:#dde2e6;
  --field:#fafafa;
  --hero-bg:#ececec;
}
*{box-sizing:border-box;margin:0;padding:0}
html,body{width:1200px;height:2276px;overflow:hidden}
body{position:relative;background:#fff;font-family:'Montserrat',sans-serif;color:var(--ink)}
.abs{position:absolute}
.brand{font-family:'Montserrat',sans-serif;font-weight:500;color:var(--orange);font-size:28px;letter-spacing:1.5px;line-height:1}
.nav a{font-size:9.5px;font-weight:500;color:#222;text-decoration:none;text-transform:uppercase;position:absolute}
.nav a.active{color:var(--blue)}
.btn-pill{border-radius:20px;display:flex;align-items:center;justify-content:center;font-weight:600;font-size:9.5px;text-decoration:none}

/* header */
.site-header{top:0;left:0;width:1200px;height:57px;background:#fff}
.signup{left:930px;top:15px;width:107px;height:28px;background:var(--orange);color:#fff}

/* hero */
.hero{top:57px;left:0;width:1200px;height:446px;background:var(--hero-bg)}
.hero-photo{top:57px;left:530px;width:670px;height:446px;background:linear-gradient(90deg,var(--hero-bg) 0%,#dfe3e6 25%,#cfd6dc 60%,#e6e9ec 100%)}
.hero-title{left:161px;top:160px;font-family:'Montserrat',sans-serif;font-weight:700;font-size:37px;color:var(--orange);line-height:1}
.hero-sub{left:161px;top:197px;font-family:'Josefin Sans',sans-serif;font-size:31px;line-height:31px;color:#222;font-weight:400}
.hero-text{left:161px;top:277px;width:345px;font-size:10.5px;line-height:16.5px;color:#333;text-align:justify}
.hero-cta{left:159px;top:352px;width:213px;height:35px;border:1.5px solid var(--orange);color:var(--orange);background:transparent}

/* features */
.sec-title{width:1200px;left:0;text-align:center;font-family:'Josefin Sans',sans-serif;font-weight:400;color:#222}
.sec-sub{width:1200px;left:0;text-align:center;font-size:10.5px;line-height:15px;color:#333}
.feature h3{font-family:'Josefin Sans',sans-serif;font-weight:400;font-size:16px;margin-bottom:6px;color:#222}
.feature p{font-size:10.3px;line-height:14px;color:#333}
.feature.left{text-align:right}
.icon{width:50px;height:46px}
.laptop{left:433px;top:720px;width:308px;height:204px}

/* pricing */
.pricing{top:1093px;left:0;width:1200px;height:615px;background:linear-gradient(160deg,#3d4651 0%,#2b323b 45%,#353d47 100%)}
.plan{width:275px;height:214px;background:#fff;border-radius:3px;overflow:hidden}
.plan h4{font-family:'Josefin Sans',sans-serif;font-weight:400;font-size:16px;text-align:center;margin-top:49px;color:#222}
.plan p{font-size:10.5px;line-height:14px;color:#444;text-align:center;padding:0 16px;margin-top:12px}
.plan .price{position:absolute;left:0;bottom:0;width:100%;height:80px;background:var(--card-band);text-align:center;padding-top:18px}
.plan .amt{font-family:'Josefin Sans',sans-serif;font-weight:700;font-size:26px;line-height:26px}
.plan .amt small{font-weight:400;font-size:13px}
.plan .per{font-family:'Josefin Sans',sans-serif;font-weight:400;font-size:13px;margin-top:2px}
.plan.featured .price{background:var(--orange);color:#fff}

/* signup form */
.field{height:36px;background:var(--field);border:1px solid #f0f0f0;box-shadow:0 2px 6px rgba(0,0,0,.06);font-size:9px;color:#888;display:flex;align-items:center;padding-left:17px}
.submit{left:520px;top:1947px;width:203px;height:41px;background:var(--blue);color:#fff;font-size:9.5px;font-weight:700;display:flex;align-items:center;justify-content:center;border-radius:2px}

/* cta band */
.cta-band{top:2042px;left:0;width:1200px;height:104px;background:var(--orange)}
.cta-text{left:160px;top:2083px;font-family:'Josefin Sans',sans-serif;font-size:22px;color:#fff}
.join{left:892px;top:2078px;width:145px;height:32px;background:#fff;color:#222}

.copyright{left:840px;top:2222px;width:198px;text-align:right;font-size:9px;font-weight:600}
</style>
</head>
<body>

<header class="abs site-header">
  <div class="abs brand" style="left:160px;top:15px">vellisto</div>
  <nav class="nav">
    <a class="active" style="left:499px;top:26px">Home</a>
    <a style="left:570px;top:26px">Products</a>
    <a style="left:661px;top:26px">Pricing</a>
  </nav>
  <a class="abs btn-pill signup">Sign up</a>
</header>

<section>
  <div class="abs hero"></div>
  <div class="abs hero-photo" role="img" aria-label="Photo of a tired doctor with a stethoscope reading papers at his desk"></div>
  <h1 class="abs hero-title">Lease Practices:</h1>
  <h2 class="abs hero-sub">Choose How You Spend<br>Your Time</h2>
  <p class="abs hero-text">Vellisto is your office operating system. Automate your painful tasks, keep track of your books, and live a little. Start with a FREE charting tool and add more products as you grow.</p>
  <a class="abs btn-pill hero-cta">Get the Charting Tool for Free</a>
</section>

<section>
  <h2 class="abs sec-title" style="top:546px;font-size:22px">AI to Automate Optometry Office Tasks</h2>
  <p class="abs sec-sub" style="top:583px">Vellisto uses AI, automation, robots, and other cool technology to streamline office work<br>so you can do things you love</p>

  <svg class="abs" style="left:380px;top:636px" width="412" height="412" viewBox="0 0 412 412">
    <circle cx="206" cy="206" r="200" fill="none" stroke="#e6e6e6" stroke-width="1"/>
  </svg>

  <div class="abs laptop" role="img" aria-label="Laptop showing the schedule screen of the app">
    <svg width="308" height="204" viewBox="0 0 308 204">
      <defs><linearGradient id="screen" x1="0" y1="0" x2="1" y2="1"><stop offset="0" stop-color="#f4f5f7"/><stop offset="1" stop-color="#e6e8eb"/></linearGradient></defs>
      <rect x="0" y="0" width="308" height="196" rx="6" fill="#d7d9dc"/>
      <rect x="8" y="10" width="292" height="180" fill="url(#screen)"/>
      <rect x="8" y="10" width="42" height="180" fill="#2f3640"/>
      <rect x="-4" y="192" width="316" height="8" rx="3" fill="#cfd2d6"/>
      <ellipse cx="154" cy="204" rx="150" ry="3" fill="#e9e9e9"/>
    </svg>
  </div>

  <div class="abs feature left" style="left:185px;top:676px;width:188px">
    <h3>Schedule</h3>
    <p>Meet your patients where they are, 24 hours 7 days a week with the online scheduler.</p>
  </div>
  <svg class="abs icon" style="left:388px;top:678px" viewBox="0 0 50 46" fill="none" stroke="#222" stroke-width="1.6">
    <circle cx="10" cy="9" r="7" stroke="var(--orange)" stroke-width="2.4"/>
    <rect x="10" y="9" width="34" height="30" rx="3"/>
    <line x1="10" y1="17" x2="44" y2="17"/>
    <line x1="18" y1="5" x2="18" y2="12"/><line x1="36" y1="5" x2="36" y2="12"/>
    <path d="M16 23h5M24 23h5M32 23h5M16 28h5M24 28h5M32 28h5M16 33h5M24 33h5M32 33h5"/>
  </svg>

  <div class="abs feature left" style="left:142px;top:793px;width:191px">
    <h3>Intake</h3>
    <p>Never print out another paper form. Your patients are now able to fill out and sign forms online.</p>
  </div>
  <svg class="abs icon" style="left:346px;top:794px" viewBox="0 0 50 46" fill="none" stroke="#222" stroke-width="1.6">
    <circle cx="10" cy="10" r="7" stroke="var(--blue)" stroke-width="2.4"/>
    <circle cx="30" cy="22" r="4"/><path d="M23 36c0-5 3-8 7-8s7 3 7 8z"/>
    <circle cx="30" cy="6" r="3"/><circle cx="46" cy="20" r="3"/><circle cx="16" cy="26" r="3"/><circle cx="44" cy="36" r="3"/>
    <path d="M30 9v9M34 21l9-1M26 23l-7 2M34 30l7 4"/>
  </svg>

  <div class="abs feature left" style="left:180px;top:907px;width:180px">
    <h3>Chart</h3>
    <p>Start charting all patient findings for FREE. With features like auto population it flies on your mobile phone.</p>
  </div>
  <svg class="abs icon" style="left:374px;top:908px" viewBox="0 0 50 46" fill="none" stroke="#222" stroke-width="1.6">
    <circle cx="10" cy="9" r="7" stroke="var(--orange)" stroke-width="2.4"/>
    <path d="M12 14h32v22H22l-6 6v-6h-4z"/>
    <path d="M20 31v-6M26 31V21M32 31v-8M38 31V19M18 31h22"/>
  </svg>

  <svg class="abs icon" style="left:735px;top:678px" viewBox="0 0 50 46" fill="none" stroke="#222" stroke-width="1.6">
    <circle cx="40" cy="9" r="7" stroke="var(--orange)" stroke-width="2.4"/>
    <path d="M14 10h22v20H14z"/><path d="M18 16h12M18 21h12M18 25h8"/>
    <path d="M8 26h28v10H8zM4 36h10"/>
  </svg>
  <div class="abs feature" style="left:802px;top:676px;width:190px">
    <h3>Bill</h3>
    <p>Don't waste your precious time or pay someone to bill insurance, let a bot do it for you.</p>
  </div>

  <svg class="abs icon" style="left:780px;top:794px" viewBox="0 0 50 46" fill="none" stroke="#222" stroke-width="1.6">
    <circle cx="36" cy="11" r="8" stroke="var(--blue)" stroke-width="2.4"/>
    <circle cx="22" cy="16" r="7"/>
    <path d="M6 38c0-9 7-14 16-14s14 4 15 10"/>
    <circle cx="38" cy="30" r="6"/><path d="M35 30l2 2 4-4"/>
    <path d="M4 38h32"/>
  </svg>
  <div class="abs feature" style="left:844px;top:793px;width:208px">
    <h3>Eligible</h3>
    <p>Don't call or login into every insurance website to get patient eligibility and copays. Our bots do that too.</p>
  </div>

  <svg class="abs icon" style="left:748px;top:908px" viewBox="0 0 50 46" fill="none" stroke="#222" stroke-width="1.6">
    <circle cx="40" cy="9" r="7" stroke="var(--orange)" stroke-width="2.4"/>
    <rect x="4" y="10" width="34" height="24" rx="2"/>
    <path d="M8 16h26"/>
    <path d="M11 22l1.5 3 3 .3-2.3 2 .7 3-2.9-1.6-2.9 1.6.7-3-2.3-2 3-.3zM21 22l1.5 3 3 .3-2.3 2 .7 3-2.9-1.6-2.9 1.6.7-3-2.3-2 3-.3zM31 22l1.5 3 3 .3-2.3 2 .7 3-2.9-1.6-2.9 1.6.7-3-2.3-2 3-.3z" stroke-width="1"/>
    <path d="M14 34v6h12"/>
  </svg>
  <div class="abs feature" style="left:814px;top:907px;width:186px">
    <h3>Review</h3>
    <p>Grow your patient base and improve your search results with the review solution.</p>
  </div>
</section>

<section>
  <div class="abs pricing" role="img" aria-label="Dark photo of a stressed man at a desk"></div>
  <h2 class="abs sec-title" style="top:1138px;font-size:22px;color:#fff">Pricing</h2>

  <div class="abs plan" style="left:161px;top:1189px">
    <h4>Free</h4>
    <p>Chart patient findings for FREE. Unlimited users, doctors, and location.</p>
    <div class="price"><div class="amt">$0</div><div class="per">No strings attached</div></div>
  </div>
  <div class="abs plan featured" style="left:462px;top:1189px">
    <h4>Pick 1 Add On</h4>
    <p>Choose between schedule, intake, bill, eligible, or review.</p>
    <div class="price"><div class="amt">$99 / <small>mo</small></div><div class="per">Per location</div></div>
  </div>
  <div class="abs plan" style="left:763px;top:1189px">
    <h4>Pick 2 Add-ons</h4>
    <p>Choose any two features between schedule, intake, bill, eligible, and/or review.</p>
    <div class="price"><div class="amt">$189 / <small>mo</small></div><div class="per">Per location</div></div>
  </div>
  <div class="abs plan" style="left:161px;top:1430px">
    <h4>Pick 3 Add-ons</h4>
    <p>Choose any three features between schedule, intake, bill, eligible, and/or review.</p>
    <div class="price"><div class="amt">$279 / <small>mo</small></div><div class="per">Per location</div></div>
  </div>
  <div class="abs plan" style="left:462px;top:1430px">
    <h4>Pick 4 Add-ons</h4>
    <p>Choose any four features between schedule, intake, bill, eligible, and/or review.</p>
    <div class="price"><div class="amt">$369 / <small>mo</small></div><div class="per">Per location</div></div>
  </div>
  <div class="abs plan" style="left:763px;top:1430px">
    <h4>Pick All Add-ons</h4>
    <p>Get all five features: schedule, intake, bill, eligible, and/or review.</p>
    <div class="price"><div class="amt">$459 / <small>mo</small></div><div class="per">Per location</div></div>
  </div>
</section>

<section>
  <h2 class="abs sec-title" style="top:1752px;font-size:28px;font-weight:700;letter-spacing:.5px">Get Started With A Free Charting Tool</h2>
  <p class="abs sec-sub" style="top:1792px">Become part of a club that wants to change the way we practice, so we can have a<br>life outside of the office.</p>

  <div class="abs field" style="left:213px;top:1850px;width:253px">Full Name</div>
  <div class="abs field" style="left:471px;top:1850px;width:253px">Email</div>
  <div class="abs field" style="left:729px;top:1850px;width:252px">Cell Phone</div>
  <div class="abs field" style="left:213px;top:1890px;width:381px">Office Name</div>
  <div class="abs field" style="left:599px;top:1890px;width:382px">Npi</div>
  <div class="abs submit">Get the Charting Tool</div>
</section>

<section>
  <div class="abs cta-band"></div>
  <div class="abs cta-text">Now spend time outside the office!</div>
  <a class="abs btn-pill join">Join The Club</a>
</section>

<footer>
  <div class="abs brand" style="left:160px;top:2198px">vellisto</div>
  <nav class="nav">
    <a class="active" style="left:837px;top:2192px">Home</a>
    <a style="left:907px;top:2192px">Products</a>
    <a style="left:998px;top:2192px">Pricing</a>
  </nav>
  <div class="abs copyright">Copyright © 2020 vellisto.com</div>
</footer>

</body>
</html>
```